Design an Elegant Handbag Brand website

I need a webiste design are looking for ideas for a new theme, color scheme, etc. You come up with the general look and feel of the home page and our team will take it from there.
We're only looking for a one (1) page layout which should be fashionable and graphic intensive, but also include the standard homepage links (about us, see our collections, etc)

Target Market(s)

Our customers are fashionable women looking for an animal friendly and environmentally friendly handbag.

Industry/Entity Type

Business

Number of Pages Required

1 page

Font styles to use
Serif
Sans Serif

Requirements
Must have
• Feel free to modify it with different colors or tweaks as you see fit. We are open to all suggestions.
Nice to have

```html
<!DOCTYPE html>
<html lang="en">
<head>
<meta charset="utf-8">
<title>LOGOHERE — Handbags</title>
<link href="https://fonts.googleapis.com/css2?family=Poppins:wght@300;400;500;600;700&display=swap" rel="stylesheet">
<style>
:root{
  --red:#e8393c;
  --peach:#fcd6b0;
  --ink:#111;
  --text:#555;
  --muted:#888;
  --cream:#fdf8f2;
  --green:#a8cc5c;
  --olive:#6a7d1c;
  --pink:#f4a7bf;
  --rose:#ecb4be;
  --gold:#b6961f;
  --purple:#8b2ad6;
  --dark:#1b1b1b;
  --line:#e8e8e8;
}
*{margin:0;padding:0;box-sizing:border-box}
html,body{width:1200px;height:4394px;overflow:hidden}
body{font-family:'Poppins',sans-serif;color:var(--ink);background:#fff;position:relative}
.abs{position:absolute}
.btn{position:absolute;display:flex;align-items:center;justify-content:center;font-size:14px;font-weight:600;text-transform:uppercase;letter-spacing:.3px}
.btn-peach{background:var(--peach);color:var(--ink)}
.btn-white{background:#fff;color:var(--ink);font-size:13px}

/* header */
.site-header{position:absolute;left:0;top:0;width:1200px;height:65px;background:#fff}
.logo{left:87px;top:19px;font-size:22px;font-weight:700;letter-spacing:.5px}
.nav a{position:absolute;top:24px;font-size:13px;font-weight:500;color:var(--ink);text-decoration:none}
.nav-icons svg{position:absolute;top:23px}

/* hero */
.hero{left:0;top:65px;width:1200px;height:736px;background:linear-gradient(90deg,#f1f1f1 0%,#ececeb 40%,#e8d48a 62%,#c58c4f 78%,#e9d163 100%)}
.hero-title{left:87px;top:348px;font-size:58px;font-weight:400;line-height:1}
.hero-sub{left:87px;top:408px;font-size:35px;font-weight:400;line-height:1}
.hero-offer{left:87px;top:448px;font-size:80px;font-weight:400;color:var(--red);line-height:1}
.dot{position:absolute;top:747px;width:14px;height:14px;border-radius:50%;border:2px solid #666;background:transparent}
.dot.active{border-color:#222;background:#fff}

/* section heads */
.kicker{left:0;width:1200px;text-align:center;color:var(--red);font-size:21px;font-weight:400}
.heading{left:0;width:1200px;text-align:center;font-size:55px;font-weight:400;line-height:1}
.intro{left:0;top:996px;width:1200px;text-align:center;font-size:17px;line-height:31px;color:var(--text)}

/* offer */
.offer{left:77px;top:1166px;width:1034px;height:528px;background:var(--cream)}
.offer-photo{left:153px;top:1145px;width:410px;height:510px;background:radial-gradient(ellipse at 50% 55%,#c98c80 0%,#b97c70 45%,#efe6e1 72%,transparent 74%)}
.offer-title{left:586px;top:1262px;font-size:55px;font-weight:400;line-height:1}
.offer-text{left:586px;top:1334px;width:480px;font-size:17px;line-height:27px;color:var(--text)}
.offer-list{position:absolute;left:586px;top:1406px;list-style:none}
.offer-list li{font-size:17px;color:var(--text);height:31px;line-height:31px;padding-left:22px;position:relative}
.offer-list li::before{content:"";position:absolute;left:0;top:11px;width:8px;height:8px;border-radius:50%;background:var(--peach)}

/* categories */
.cat{position:absolute}
.cat-green{left:89px;top:1909px;width:504px;height:414px;background:var(--green)}
.cat-green-photo{left:340px;top:1925px;width:250px;height:360px;background:radial-gradient(ellipse at 55% 70%,#c8202a 0%,#b01a22 30%,transparent 55%)}
.cat-pink{left:608px;top:1909px;width:503px;height:201px;background:var(--pink)}
.cat-rose{left:608px;top:2122px;width:503px;height:201px;background:var(--rose)}
.cat-pink-photo{left:850px;top:1930px;width:220px;height:170px;background:radial-gradient(ellipse at 50% 60%,#f2e23a 0%,#e8d83a 35%,transparent 60%)}
.cat-rose-photo{left:860px;top:2140px;width:220px;height:180px;background:radial-gradient(ellipse at 45% 70%,#9a3ad0 0%,#7d2fb3 35%,transparent 62%)}
.sale-kicker{left:116px;top:2068px;font-size:17px;font-weight:700;color:var(--red)}
.sale-upto{left:112px;top:2115px;font-size:17px;font-weight:700;color:var(--olive);transform:rotate(-90deg);transform-origin:left top;top:2165px}
.sale-num{left:142px;top:2086px;font-size:88px;font-weight:700;color:var(--olive);line-height:1}
.sale-pct{left:276px;top:2096px;font-size:30px;font-weight:700;color:var(--olive);line-height:1}
.sale-off{left:256px;top:2130px;font-size:30px;font-weight:700;color:var(--olive);line-height:1}
.cat-label{font-size:17px;font-weight:500;color:#333}
.cat-deal{font-size:25px;font-weight:700}

/* banner */
.banner{left:0;top:2439px;width:1200px;height:500px;background:linear-gradient(90deg,#b08058 0%,#c4956c 14%,#5a3a30 20%,#4e3129 50%,#5a3a30 85%,#d8d4cc 90%,#eeeeea 100%)}
.banner-kicker{left:0;top:2622px;width:1200px;text-align:center;color:#fff;font-size:30px}
.banner-title{left:0;top:2656px;width:1200px;text-align:center;color:#fff;font-size:76px;line-height:1}
.banner-sub{left:0;top:2734px;width:1200px;text-align:center;color:#fff;font-size:32px}

/* products */
.product{position:absolute;top:3179px;height:331px;border:1px solid var(--line);background:#fff}
.product-photo{position:absolute;left:50%;top:34px;width:150px;height:170px;transform:translateX(-50%)}
.stars{position:absolute;left:0;width:100%;text-align:center;font-size:13px;color:#ddd;letter-spacing:3px}
.product-name{position:absolute;left:0;width:100%;text-align:center;font-size:15px;font-weight:600}
.product-price{position:absolute;left:0;width:100%;text-align:center;font-size:22px;font-weight:600;color:var(--red)}
.cart-btn{left:40px;top:295px;width:129px;height:33px;font-size:12px;font-weight:500}
.heart{position:absolute;left:169px;top:295px;width:31px;height:33px;background:#111;display:flex;align-items:center;justify-content:center}

/* features */
.feature-title{font-size:19px;font-weight:600;color:#222}
.feature-text{font-size:13px;line-height:17px;color:#555;width:230px}

/* footer */
.footer{left:0;top:3854px;width:1200px;height:540px;background:var(--dark)}
.news-title{left:85px;top:3908px;font-size:39px;font-weight:700;color:#fff;line-height:1}
.news-sub{left:87px;top:3954px;font-size:16px;color:#fff;font-weight:500}
.news-form{left:562px;top:3915px;width:546px;height:50px;background:#2b2b2b}
.news-input{position:absolute;left:22px;top:15px;font-size:13px;color:#ccc;display:flex;align-items:center;gap:7px}
.news-btn{right:4px;top:5px;width:120px;height:40px;font-size:13px}
.rule{position:absolute;left:89px;width:1022px;height:1px;background:#333}
.foot-h{font-size:17px;font-weight:600;color:#fff}
.foot-list{position:absolute;list-style:none}
.foot-list li{font-size:13px;color:#aaa;height:27px;line-height:27px}
.contact-row{position:absolute;left:915px;display:flex;gap:14px;font-size:13px;color:#aaa;line-height:17px}
.copy{left:89px;top:4349px;font-size:13px;color:#fff}
.social{position:absolute;top:4353px;width:10px;height:10px;border-radius:50%;background:#fff}
.pay{position:absolute;top:4344px;width:40px;height:26px;border-radius:4px}
.to-top{left:1136px;top:4306px;width:34px;height:34px;border-radius:50%;background:var(--red);display:flex;align-items:center;justify-content:center}
</style>
</head>
<body>

<header class="site-header">
  <div class="abs logo">LOGOHERE</div>
  <nav class="nav">
    <a style="left:533px">HOME</a>
    <a style="left:617px">ABOUT US</a>
    <a style="left:728px">OUR SHOP</a>
    <a style="left:842px">BLOG</a>
    <a style="left:922px">CONTACT US</a>
  </nav>
  <div class="nav-icons">
    <svg style="left:1043px" width="16" height="14" viewBox="0 0 16 14"><path d="M0 1h3l2 8h9l2-6H4" fill="none" stroke="#111" stroke-width="2"/><circle cx="6" cy="12" r="1.5" fill="#111"/><circle cx="13" cy="12" r="1.5" fill="#111"/></svg>
    <svg style="left:1071px" width="13" height="14" viewBox="0 0 13 14"><circle cx="6.5" cy="4" r="3.5" fill="#111"/><path d="M0 14c0-5 13-5 13 0z" fill="#111"/></svg>
    <svg style="left:1099px" width="14" height="14" viewBox="0 0 14 14"><circle cx="6" cy="6" r="4.5" fill="none" stroke="#111" stroke-width="2"/><path d="M9 9l4 4" stroke="#111" stroke-width="2"/></svg>
  </div>
</header>

<section>
  <div class="abs hero" role="img" aria-label="Woman in a yellow floral dress carrying a tan leather crossbody bag with a silk scarf"></div>
  <h1 class="abs hero-title">TRENDY BACKPACK</h1>
  <div class="abs hero-sub">OWN STYLE</div>
  <div class="abs hero-offer">50%OFF</div>
  <a class="btn btn-peach" style="left:90px;top:530px;width:138px;height:48px">Shop now</a>
  <span class="dot active" style="left:569px"></span>
  <span class="dot" style="left:593px"></span>
  <span class="dot" style="left:617px"></span>
</section>

<section>
  <div class="abs kicker" style="top:900px">WELCOME</div>
  <h2 class="abs heading" style="top:928px">TO OUR STORE!</h2>
  <p class="abs intro">Lorem Ipsum is simply dummy text of the printing and typesetting industry.<br>Lorem Ipsum has been the industry's standard dummy text ever since the 1500s,<br>when an unknown printer took .</p>
</section>

<section>
  <div class="abs offer"></div>
  <div class="abs offer-photo" role="img" aria-label="Dusty pink leather handbag with a marbled tag"></div>
  <h2 class="abs offer-title">WHAT WE OFFER</h2>
  <p class="abs offer-text">Lorem Ipsum is simply dummy text of the printing and typesetting industry.</p>
  <ul class="offer-list">
    <li>Cozy atmosphere</li>
    <li>Customer-friendly service</li>
    <li>Quality guarantee</li>
    <li>100% satisfaction</li>
    <li>Special offers</li>
    <li>Free delivery</li>
  </ul>
</section>

<section>
  <div class="abs kicker" style="top:1795px">BROWSE OUR</div>
  <h2 class="abs heading" style="top:1822px">CATEGORIES</h2>

  <div class="cat cat-green"></div>
  <div class="abs cat-green-photo" role="img" aria-label="Red leather saddle bag with a long strap and a red wallet"></div>
  <div class="abs sale-kicker">END OF SEASON SALE</div>
  <div class="abs sale-upto">UP TO</div>
  <div class="abs sale-num">50</div>
  <div class="abs sale-pct">%</div>
  <div class="abs sale-off">OFF</div>
  <a class="btn btn-white" style="left:114px;top:2183px;width:126px;height:35px">Shop now</a>

  <div class="cat cat-pink"></div>
  <div class="abs cat-pink-photo" role="img" aria-label="Yellow and white shoulder bag with a gold chain"></div>
  <div class="abs cat-label" style="left:653px;top:1962px">SHOULDER BAGS</div>
  <div class="abs cat-deal" style="left:653px;top:1982px;color:var(--gold)">MIN. 30% OFF</div>
  <a class="btn btn-white" style="left:655px;top:2025px;width:126px;height:34px">Shop now</a>

  <div class="cat cat-rose"></div>
  <div class="abs cat-rose-photo" role="img" aria-label="Purple sequin hobo bag with a phone and earphones"></div>
  <div class="abs cat-label" style="left:655px;top:2175px">HOBO BAGS</div>
  <div class="abs cat-deal" style="left:655px;top:2195px;color:var(--purple)">MIN. 30% OFF</div>
  <a class="btn btn-white" style="left:655px;top:2238px;width:126px;height:34px">Shop now</a>
</section>

<section>
  <div class="abs banner" role="img" aria-label="Woman in a camel coat holding a black leather backpack by a wooden door"></div>
  <div class="abs banner-kicker">DESIGNER BAGS COLLECTION</div>
  <h2 class="abs banner-title">MORE SHAPES,</h2>
  <div class="abs banner-sub">MORE STYLES, MORE CREATIVE DESIGNS!</div>
</section>

<section>
  <div class="abs kicker" style="top:3057px">WEEKLY</div>
  <h2 class="abs heading" style="top:3084px">FEATURED PRODUCTS</h2>

  <article class="product" style="left:89px;width:236px">
    <div class="product-photo" role="img" aria-label="Beige tote with brown handles" style="background:radial-gradient(ellipse at 50% 60%,#d9a98f 0%,#c99479 40%,transparent 65%)"></div>
    <div class="stars" style="top:233px">★★★★★</div>
    <div class="product-name" style="top:258px">PRODUCT HEADING</div>
    <div class="product-price" style="top:279px">$10.00</div>
  </article>
  <article class="product" style="left:349px;width:240px">
    <div class="product-photo" role="img" aria-label="Black structured top-handle bag" style="top:20px;background:radial-gradient(ellipse at 50% 55%,#2b2b2b 0%,#333 40%,transparent 65%)"></div>
    <div class="stars" style="top:206px">★★★★★</div>
    <div class="product-name" style="top:231px">PRODUCT HEADING</div>
    <div class="product-price" style="top:252px">$10.00</div>
    <a class="btn btn-peach cart-btn">Add to cart</a>
    <div class="heart"><svg width="13" height="12" viewBox="0 0 13 12"><path d="M6.5 12L1 6.5A3 3 0 0 1 6.5 2a3 3 0 0 1 5.5 4.5z" fill="#fff"/></svg></div>
  </article>
  <article class="product" style="left:608px;width:238px">
    <div class="product-photo" role="img" aria-label="Navy duffel bag with tan handles" style="background:radial-gradient(ellipse at 50% 62%,#1f2a44 0%,#27324c 40%,transparent 62%)"></div>
    <div class="stars" style="top:233px">★★★★★</div>
    <div class="product-name" style="top:258px">PRODUCT HEADING</div>
    <div class="product-price" style="top:279px">$10.00</div>
  </article>
  <article class="product" style="left:873px;width:238px">
    <div class="product-photo" role="img" aria-label="Mauve leather satchel" style="background:radial-gradient(ellipse at 50% 60%,#b46b95 0%,#a45f88 40%,transparent 65%)"></div>
    <div class="stars" style="top:233px">★★★★★</div>
    <div class="product-name" style="top:258px">PRODUCT HEADING</div>
    <div class="product-price" style="top:279px">$10.00</div>
  </article>
</section>

<section>
  <svg class="abs" style="left:87px;top:3648px" width="66" height="52" viewBox="0 0 66 52" fill="none" stroke="#333" stroke-width="2"><circle cx="20" cy="20" r="18"/><path d="M2 20h36M20 2c-8 10-8 26 0 36M20 2c8 10 8 26 0 36"/><rect x="26" y="26" width="22" height="16" fill="#fff"/><path d="M48 30h9l6 7v5H48z" fill="#fff"/><circle cx="33" cy="44" r="4" fill="#fff"/><circle cx="55" cy="44" r="4" fill="#fff"/></svg>
  <div class="abs feature-title" style="left:170px;top:3650px">Free delivery</div>
  <div class="abs feature-text" style="left:170px;top:3686px">Lorem ipsum dolor sit amet elit sed do eiusmod dummy.</div>

  <svg class="abs" style="left:462px;top:3646px" width="48" height="58" viewBox="0 0 48 58" fill="none" stroke="#333" stroke-width="2"><rect x="16" y="2" width="24" height="32" rx="2"/><circle cx="28" cy="14" r="5"/><path d="M2 40l10-8h14c3 0 3 5 0 5H16M2 56l8-6h16l14-12c2-2 5 1 3 3L30 56"/></svg>
  <div class="abs feature-title" style="left:537px;top:3650px">Sale &amp; Discounts</div>
  <div class="abs feature-text" style="left:537px;top:3686px">Lorem ipsum dolor sit amet elit sed do eiusmod dummy.</div>

  <svg class="abs" style="left:811px;top:3648px" width="60" height="56" viewBox="0 0 60 56" fill="none" stroke="#333" stroke-width="2"><circle cx="40" cy="20" r="14"/><text x="40" y="24" font-size="10" text-anchor="middle" fill="#333" stroke="none" font-family="Poppins,sans-serif">24/7</text><path d="M8 14c-6 6 0 24 14 34 5 4 10 4 12 0l-6-7-5 3c-5-3-10-10-11-15l5-3-3-9c-2-3-4-4-6-3z"/></svg>
  <div class="abs feature-title" style="left:892px;top:3650px">Service Online</div>
  <div class="abs feature-text" style="left:892px;top:3686px">Lorem ipsum dolor sit amet elit sed do eiusmod dummy.</div>
</section>

<footer>
  <div class="abs footer"></div>
  <div class="abs news-title">Newsletter</div>
  <div class="abs news-sub">Subscribe to our newsletter</div>
  <div class="abs news-form">
    <div class="news-input"><svg width="14" height="10" viewBox="0 0 14 10"><rect width="14" height="10" fill="#bbb"/><path d="M0 0l7 6 7-6" stroke="#2b2b2b" fill="none"/></svg>Enter your email address</div>
    <a class="btn btn-peach news-btn">Subscribe</a>
  </div>
  <div class="rule" style="top:4017px"></div>

  <div class="abs foot-h" style="left:118px;top:4088px">INFORMATION</div>
  <ul class="foot-list" style="left:118px;top:4126px"><li>My account</li><li>Wishlist</li><li>Checkout</li><li>Cart</li><li>Contact</li></ul>

  <div class="abs foot-h" style="left:408px;top:4088px">QUICK LINKS</div>
  <ul class="foot-list" style="left:408px;top:4115px"><li>Home</li><li>About Us</li><li>Collections</li><li>Product</li><li>Shop</li></ul>

  <div class="abs foot-h" style="left:657px;top:4088px">SUPPORT</div>
  <ul class="foot-list" style="left:657px;top:4126px"><li>Terms of use</li><li>Terms and Conditions</li><li>Privacy Policy</li><li>Returns</li><li>Refunds.</li></ul>

  <div class="abs foot-h" style="left:916px;top:4088px">CONTACT US</div>
  <div class="contact-row" style="top:4131px"><svg width="11" height="11" viewBox="0 0 11 11"><path d="M2 0l2 3-1 1.5c1 2 2 3 3.5 3.5L8 7l3 2-1 2C5 11 0 6 0 1z" fill="var(--peach)"/></svg>123-456-7890</div>
  <div class="contact-row" style="top:4169px"><svg width="12" height="9" viewBox="0 0 12 9"><rect width="12" height="9" fill="var(--peach)"/><path d="M0 0l6 5 6-5" stroke="#1b1b1b" fill="none"/></svg>info@example.com</div>
  <div class="contact-row" style="top:4208px"><svg width="10" height="13" viewBox="0 0 10 13"><path d="M5 13C1 8 0 6 0 5a5 5 0 0 1 10 0c0 1-1 3-5 8z" fill="var(--peach)"/><circle cx="5" cy="5" r="2" fill="#1b1b1b"/></svg><span>Some address line goes<br>city name country</span></div>

  <div class="abs to-top"><svg width="10" height="7" viewBox="0 0 10 7"><path d="M1 6l4-4 4 4" stroke="#fff" stroke-width="1.6" fill="none"/></svg></div>
  <div class="rule" style="top:4324px"></div>
  <div class="abs copy">© Copyright 2020 All Right Reserved</div>
  <span class="social" style="left:567px"></span>
  <span class="social" style="left:612px"></span>
  <span class="social" style="left:657px"></span>
  <span class="pay" style="left:967px;background:#f2f2f2"></span>
  <span class="pay" style="left:1017px;background:#1a2a8c"></span>
  <span class="pay" style="left:1067px;background:#f2f2f2"></span>
</footer>

</body>
</html>
```